Plain Larder 100% real ingredients

I need a label design for my hummus.
"Big Whoa" Hummus
Roasted Red Pepper hummus infused with Crushed Red Pepper for a kick
Made With Real Ingredients
Oil Free
Preservative Free
in small print: PlainLarderNaturalFoods.example
I also need an ingredient list
Chickpeas, Tahini, Red bell pepper, Sweet onion, Garlic, Water, Lemon, Maple syrup, Crushed red pepper, Pink Himalayan salt, Cumin, Cayenne, Black pepper,Baking soda
In our Hummus:
We believe that our hummus doesn't need all the extra ingredients like oils and preservatives. We want you to feel good after eating our products while also eating good food that is good for you! So we use fresh ingredients like lemon, garlic, red peppers, and sweet onions.
In the design can you put a red roasted pepper in the background?
Two of the pictures I uploaded are examples of what I would like it to look like.

```html
<!DOCTYPE html>
<html lang="en">
<head>
<meta charset="utf-8">
<title>Big Whoa Hummus – Label</title>
<link rel="stylesheet" href="https://fonts.googleapis.com/css2?family=DM+Serif+Display&family=Noto+Serif:wght@700&family=Kaushan+Script&display=swap">
<style>
  :root {
    --page-bg: #e9ebef;
    --label-bg: #e4e6e8;
    --brand-red: #a81c24;
    --brand-red-light: #c0262e;
    --script-red: #ad1f2a;
    --ink: #111111;
    --subtitle-grey: #6a6a6a;
    --panel-black: #1c1c1c;
    --white: #ffffff;
  }
  * { margin: 0; padding: 0; box-sizing: border-box; }
  html, body {
    width: 1200px; height: 912px; overflow: hidden;
    background: var(--page-bg);
  }
  .label {
    position: absolute; left: 40px; top: 182px;
    width: 1120px; height: 548px;
    background: linear-gradient(180deg, #eceef0 0%, var(--label-bg) 100%);
    overflow: hidden;
    box-shadow: 0 6px 24px rgba(0,0,0,0.12);
  }
  .claims-strip {
    position: absolute; left: 0; top: 0; width: 232px; height: 422px;
    background: linear-gradient(180deg, var(--brand-red-light) 0%, var(--brand-red) 100%);
  }
  .claim {
    position: absolute; left: 0; width: 232px; text-align: center;
    color: var(--white);
    font-family: "Noto Serif", serif; font-weight: 700;
    font-size: 21px; line-height: 28px;
  }
  .claim svg { display: block; margin: 0 auto 4px; }
  .claim--oil { top: 37px; }
  .claim--preservative { top: 205px; }
  .net-weight {
    position: absolute; left: 0; top: 422px; width: 232px; height: 126px;
    background: var(--panel-black); color: var(--white);
    font-family: "Noto Serif", serif; font-weight: 700;
    padding: 16px 0 0 66px;
  }
  .net-weight__caption { font-size: 22px; line-height: 30px; }
  .net-weight__value { font-size: 38px; line-height: 46px; }
  .brand {
    position: absolute; left: 288px; top: 148px;
    display: flex; align-items: center; gap: 12px;
    font-family: "DM Serif Display", serif; font-size: 36px;
    color: var(--ink); white-space: nowrap;
  }
  .brand__dot {
    width: 22px; height: 22px; border-radius: 50%;
    border: 2px solid var(--ink); flex: none;
  }
  .pepper-plate {
    position: absolute; left: 577px; top: -64px;
    width: 450px; height: 450px; border-radius: 50%;
    background: radial-gradient(circle at 62% 40%, #c8331f 0%, #b02a1a 28%, #d7d9dc 46%, #cfd2d6 100%);
  }
  .tagline {
    position: absolute; left: 588px; top: 274px;
    font-family: "Kaushan Script", cursive; font-size: 44px;
    color: var(--script-red); transform: rotate(-3deg);
    white-space: nowrap;
  }
  .product-name {
    position: absolute; left: 266px; top: 334px;
    font-family: "DM Serif Display", serif; font-size: 90px; line-height: 104px;
    color: var(--ink); white-space: nowrap; letter-spacing: 0.5px;
  }
  .product-description {
    position: absolute; left: 280px; top: 436px;
    font-family: "Noto Serif", serif; font-weight: 700;
    font-size: 30px; line-height: 40px; color: var(--subtitle-grey);
    white-space: nowrap;
  }
</style>
</head>
<body>
  <main class="label">
    <aside class="claims-strip">
      <div class="claim claim--oil">
        <svg width="86" height="86" viewBox="0 0 86 86" aria-hidden="true">
          <circle cx="43" cy="43" r="40" fill="none" stroke="#fff" stroke-width="3"/>
          <path d="M43 18 C36 30 29 40 29 50 a14 14 0 0 0 28 0 C57 40 50 30 43 18Z" fill="#fff"/>
          <line x1="15" y1="15" x2="71" y2="71" stroke="#fff" stroke-width="3"/>
        </svg>
        Oil<br>free
      </div>
      <div class="claim claim--preservative">
        <svg width="86" height="86" viewBox="0 0 86 86" aria-hidden="true">
          <circle cx="43" cy="43" r="40" fill="none" stroke="#fff" stroke-width="3"/>
          <path d="M37 30 h12 M39 30 v14 l-12 20 h32 l-12 -20 v-14" fill="none" stroke="#fff" stroke-width="3" stroke-linejoin="round"/>
          <path d="M31 58 l-4 6 h32 l-4 -6Z" fill="#fff"/>
          <circle cx="43" cy="22" r="2" fill="#fff"/><circle cx="40" cy="15" r="1.6" fill="#fff"/>
          <line x1="15" y1="15" x2="71" y2="71" stroke="#fff" stroke-width="3"/>
        </svg>
        Preservative<br>free
      </div>
    </aside>
    <div class="net-weight">
      <div class="net-weight__caption">Net Wt.:</div>
      <div class="net-weight__value">160g</div>
    </div>

    <div class="brand"><span class="brand__dot"></span>Plain Larder</div>

    <div class="pepper-plate" role="img" aria-label="Roasted red bell peppers with grill marks on a white plate"></div>

    <p class="tagline">Made with real ingredients</p>
    <h1 class="product-name">Big Whoa Hummus</h1>
    <p class="product-description">Roasted Red Pepper hummus infused with<br>Crushed Red Pepper for a kick</p>
  </main>
</body>
</html>
```